HearthBay business card and stationary design

We are looking for a simple yet elegant design for our mortgage company business card and stationary.

The card should include:
Name (Doug Warley)
Title (CEO)
Phone Number (614-382-9047)
Address (48 Birchwood Terrace, Suite 315, Marlow, NJ 08214)
Email (email@hearthbay.example)
"NMLS" i.e. (NMLS 61947)
"Company NMLS" (Company NMLS 492716)

Contact Information for Business Card

See above

```html
<!DOCTYPE html>
<html lang="en">
<head>
<meta charset="utf-8">
<title>HearthBay Business Card</title>
<link rel="stylesheet" href="https://fonts.googleapis.com/css2?family=Montserrat:wght@500;700&family=Arimo:wght@400&display=swap">
<style>
  :root {
    --backdrop: #2b2b2d;
    --card: #0c0c0d;
    --brand-blue: #1ba4e6;
    --ink-white: #f4f6f8;
    --divider: #3a3a3c;
  }
  * { margin: 0; padding: 0; box-sizing: border-box; }
  html, body {
    width: 1200px; height: 900px; overflow: hidden;
    background: var(--backdrop);
  }
  .canvas {
    position: relative; width: 1200px; height: 900px;
  }
  .card {
    position: absolute; left: 250px; width: 700px; height: 400px;
    background: var(--card);
    box-shadow: 0 14px 30px rgba(0,0,0,0.55);
  }
  .card--front { top: 40px; }
  .card--back { top: 470px; }

  .wordmark {
    font-family: "Montserrat", sans-serif;
    font-weight: 500;
    color: var(--ink-white);
    letter-spacing: 0.5px;
    line-height: 1;
    white-space: nowrap;
  }
  .card--front .wordmark {
    position: absolute; left: 52px; top: 168px; font-size: 46px;
  }
  .card--back .wordmark {
    position: absolute; left: 0; right: 0; top: 170px;
    text-align: center; font-size: 64px;
  }

  .divider {
    position: absolute; left: 330px; top: 70px;
    width: 1px; height: 220px; background: var(--divider);
  }

  .contact {
    position: absolute; left: 362px; top: 78px;
    font-family: "Arimo", sans-serif; color: var(--ink-white);
  }
  .contact__name {
    font-family: "Montserrat", sans-serif; font-weight: 700;
    color: var(--brand-blue); font-size: 27px; line-height: 1.05;
  }
  .contact__title { font-size: 17px; margin-bottom: 14px; }
  .contact__list { list-style: none; }
  .contact__item {
    display: flex; align-items: center; gap: 8px;
    font-size: 15.5px; line-height: 22px;
  }
  .contact__icon { width: 15px; height: 15px; flex: none; }
  .contact__accent { color: var(--brand-blue); }
  .contact__address {
    margin-top: 16px; font-size: 15.5px; line-height: 21px; font-style: normal;
  }

  .licensing {
    position: absolute; left: 0; right: 0; bottom: 38px;
    text-align: center;
    font-family: "Arimo", sans-serif; font-size: 17px;
    color: var(--ink-white); letter-spacing: 0.3px;
  }
  .licensing__label { color: var(--brand-blue); }
  .licensing__sep { margin: 0 10px; }
</style>
</head>
<body>
<main class="canvas">
  <section class="card card--front" aria-label="Business card front">
    <div class="wordmark">HearthBay</div>
    <div class="divider"></div>
    <div class="contact">
      <div class="contact__name">Doug Warley</div>
      <div class="contact__title">CEO</div>
      <ul class="contact__list">
        <li class="contact__item">
          <svg class="contact__icon" viewBox="0 0 24 24" aria-hidden="true"><path fill="var(--brand-blue)" d="M6.6 10.8a15.1 15.1 0 0 0 6.6 6.6l2.2-2.2a1 1 0 0 1 1-.25 11.4 11.4 0 0 0 3.6.57 1 1 0 0 1 1 1V20a1 1 0 0 1-1 1A17 17 0 0 1 3 4a1 1 0 0 1 1-1h3.5a1 1 0 0 1 1 1c0 1.25.2 2.45.57 3.57a1 1 0 0 1-.25 1z"/></svg>
          <span>614-382-9047</span>
        </li>
        <li class="contact__item">
          <svg class="contact__icon" viewBox="0 0 24 24" aria-hidden="true"><rect x="2" y="5" width="20" height="14" fill="var(--brand-blue)"/><path d="M2 5l10 8 10-8" fill="none" stroke="var(--card)" stroke-width="1.8"/></svg>
          <span>email@hearthbay.example</span>
        </li>
        <li class="contact__item">
          <svg class="contact__icon" viewBox="0 0 24 24" aria-hidden="true"><g fill="none" stroke="var(--brand-blue)" stroke-width="2"><circle cx="12" cy="12" r="9.5"/><ellipse cx="12" cy="12" rx="4" ry="9.5"/><path d="M2.5 12h19M4 7h16M4 17h16"/></g></svg>
          <span>www.<span class="contact__accent">hearthbay</span>.example</span>
        </li>
      </ul>
      <address class="contact__address">48 Birchwood Terrace, Suite 315<br>Marlow, NJ 08214</address>
    </div>
    <div class="licensing">
      <span class="licensing__label">NMLS</span> 61947<span class="licensing__sep">|</span><span class="licensing__label">Company NMLS</span> 492716
    </div>
  </section>

  <section class="card card--back" aria-label="Business card back">
    <div class="wordmark">HearthBay</div>
  </section>
</main>
</body>
</html>
```